Quillex Landing Page & Logo

We are building a landing page for a new blockchain-based project called Quillex. The site should look modern and minimalistic with a very brief description of the upcoming project ("Unlock your Brevitan governance stack. Win weekly prizes and a quarterly jackpot!"), a viper logo (the animal - but can just be lettering) , and a button to subscribe for updates and early access.
Examples of similar pages:
https://pondru.finance/
https://www.zentrimo.org/
https://lumbrecks.com/
https://q8.io/
https://www.tovern.finance/
Crypto Users (Specifically Brevitan holders)

```html
<!DOCTYPE html>
<html lang="en">
<head>
<meta charset="utf-8">
<title>Quillex</title>
<link rel="stylesheet" href="https://fonts.googleapis.com/css2?family=Poppins:wght@400;500;600;700;800&family=Montserrat:wght@400;500&display=swap">
<style>
:root{
  --navy-deep:#03041c;
  --navy:#0a0f5e;
  --navy-bright:#12168a;
  --ink:#15178a;
  --gold:#fbb824;
  --orange-top:#fdb526;
  --orange-bottom:#fb8a1c;
  --white:#ffffff;
  --text:#333333;
  --muted:#8a8a8a;
  --dark:#1b1b2b;
  --field:#e8e8e8;
}
*{margin:0;padding:0;box-sizing:border-box}
html,body{width:692px;height:1200px;overflow:hidden;background:var(--white)}
body{position:relative;font-family:"Poppins",sans-serif;color:var(--text)}

.hero{position:absolute;left:0;top:0;width:692px;height:389px;
  background:radial-gradient(ellipse at 68% 45%,#1637b8 0%,#0b1a78 35%,#050a3a 70%,var(--navy-deep) 100%);overflow:hidden}
.hero-art{position:absolute;left:361px;top:71px;width:285px;height:271px;border-radius:14px;
  background:radial-gradient(circle at 48% 52%,#d99a3e 0%,#b56a22 18%,#2a5ee8 38%,#1230a8 70%,rgba(10,26,120,0) 100%)}
.brand{position:absolute;font-weight:700;color:var(--white);font-size:19px;letter-spacing:-.2px}
.hero .brand{left:94px;top:22px}
.headline{position:absolute;left:93px;top:102px;width:280px;font-weight:800;font-size:33px;line-height:34.5px;color:var(--white);text-transform:uppercase;letter-spacing:-.3px}
.headline .accent{color:var(--gold)}
.tagline{position:absolute;left:94px;top:254px;font-weight:500;font-size:12.4px;color:var(--white)}
.cta{position:absolute;left:94px;top:298px;width:135px;height:25px;border-radius:13px;
  background:linear-gradient(180deg,var(--orange-top),var(--orange-bottom));color:var(--white);
  font-weight:500;font-size:8.6px;display:flex;align-items:center;justify-content:center;text-transform:uppercase}

.features{position:absolute;left:0;top:389px;width:692px;height:468px}
.section-title{position:absolute;left:0;width:692px;text-align:center;font-weight:600;font-size:27px;color:var(--ink)}
.features .section-title{top:27px}
.lead{position:absolute;left:100px;top:68px;width:492px;text-align:center;font-size:13.6px;line-height:21.5px;color:var(--text)}
.feature{position:absolute;width:160px;text-align:center}
.feature .badge{display:block;width:74px;height:74px;margin:0 auto}
.feature h3{margin-top:10px;font-weight:600;font-size:8.6px;line-height:12px;color:var(--dark)}
.feature p{margin-top:6px;font-family:"Montserrat",sans-serif;font-size:7.2px;line-height:12px;color:var(--muted)}
.f1{left:84px;top:130px}.f2{left:265px;top:130px}.f3{left:446px;top:130px}
.f4{left:84px;top:289px}.f5{left:265px;top:289px}.f6{left:446px;top:289px}

.partners{position:absolute;left:0;top:857px;width:692px;height:154px;
  background:linear-gradient(180deg,var(--navy-deep) 0%,var(--navy) 60%,var(--navy-bright) 100%)}
.partners .section-title{top:21px;color:var(--white)}
.partner-row{position:absolute;left:94px;top:83px;width:505px;display:flex;justify-content:space-between;align-items:center}
.partner{display:flex;align-items:center;gap:5px;color:var(--white);font-weight:600;font-size:19px;letter-spacing:-.5px}
.partner .dot{width:18px;height:18px;border-radius:50%;background:var(--white)}

.newsletter{position:absolute;left:0;top:1011px;width:692px;height:121px}
.newsletter h2{position:absolute;left:93px;top:41px;font-weight:500;font-size:13.4px;letter-spacing:.4px;color:var(--ink)}
.newsletter .note{position:absolute;left:94px;top:66px;font-family:"Montserrat",sans-serif;font-size:5px;color:var(--dark)}
.email{position:absolute;left:345px;top:43px;width:253px;height:30px;background:var(--field);
  display:flex;align-items:center;justify-content:space-between;padding:0 13px}
.email span{font-family:"Montserrat",sans-serif;font-size:7.8px;letter-spacing:.5px;color:#8c8c8c}
.email svg{width:13px;height:13px}

.footer{position:absolute;left:0;top:1132px;width:692px;height:68px;background:linear-gradient(180deg,var(--navy-bright),#0a0c4a)}
.footer .brand{left:93px;top:21px}
.social{position:absolute;right:94px;top:27px;display:flex;gap:18px}
.social span{color:var(--orange-top);font-weight:600;font-size:9px}
</style>
</head>
<body>

<header class="hero">
  <div class="hero-art" role="img" aria-label="Glowing golden padlock inside a blue wireframe cube on a digital circuit background"></div>
  <div class="brand">Quillex</div>
  <h1 class="headline"><span class="accent">Unlock</span> your Brevitan governance stack.</h1>
  <p class="tagline">Win weekly prizes and a quarterly jackpot!</p>
  <a class="cta">Subscribe for updates</a>
</header>

<section class="features">
  <h2 class="section-title">Fast &amp; Secure</h2>
  <p class="lead">Quillex is instilling the advantages of blockchain settlement technology into the FX industry in a regulatory-compliant manner.</p>

  <svg width="0" height="0" style="position:absolute">
    <defs>
      <linearGradient id="badgeFill" x1="0" y1="0" x2="0" y2="1">
        <stop offset="0" stop-color="#fdb526"/><stop offset="1" stop-color="#fb8a1c"/>
      </linearGradient>
    </defs>
  </svg>

  <div class="feature f1">
    <svg class="badge" viewBox="0 0 74 74"><circle cx="37" cy="37" r="37" fill="url(#badgeFill)"/>
      <g fill="#fff"><circle cx="35" cy="31" r="8"/><path d="M22 55v-6c0-6 6-9 13-9s13 3 13 9v6z"/><path d="M52 14v10h-4l6 7 6-7h-4V14z"/></g>
      <rect x="33.5" y="26" width="3" height="6" fill="#fb9a20"/><rect x="33.5" y="34" width="3" height="2.5" fill="#fb9a20"/>
    </svg>
    <h3>Reduced<br>counter-party risk</h3>
    <p>Ut enim ad minim veniam,<br>quis nostrud exercitation ullamco</p>
  </div>

  <div class="feature f2">
    <svg class="badge" viewBox="0 0 74 74"><circle cx="37" cy="37" r="37" fill="url(#badgeFill)"/>
      <rect x="22" y="19" width="27" height="36" fill="#fff"/>
      <g stroke="#fb9a20" stroke-width="1.5"><path d="M26 26h19M26 31h19M26 36h15M26 41h12M26 46h12"/></g>
      <path d="M50 35l8 3v7c0 5-4 8-8 10-4-2-8-5-8-10v-7z" fill="#fff" stroke="#fb9a20" stroke-width="1.5"/>
      <path d="M46 45l3 3 5-6" fill="none" stroke="#fb9a20" stroke-width="1.8"/>
    </svg>
    <h3>Regulatory &amp;<br>Compliance Adaption</h3>
    <p>Ut enim ad minim veniam,<br>quis nostrud exercitation ullamco</p>
  </div>

  <div class="feature f3">
    <svg class="badge" viewBox="0 0 74 74"><circle cx="37" cy="37" r="37" fill="url(#badgeFill)"/>
      <g fill="#fff"><ellipse cx="33" cy="22" rx="12" ry="5"/><rect x="21" y="27" width="24" height="5" rx="2.5"/><rect x="21" y="34" width="24" height="5" rx="2.5"/><rect x="21" y="41" width="24" height="5" rx="2.5"/><circle cx="47" cy="44" r="12"/></g>
      <text x="47" y="49" text-anchor="middle" font-family="Poppins,sans-serif" font-weight="700" font-size="14" fill="#fb9a20">$</text>
    </svg>
    <h3>Fiat to<br>DeFi on-ramps</h3>
    <p>Ut enim ad minim veniam,<br>quis nostrud exercitation ullamco</p>
  </div>

  <div class="feature f4">
    <svg class="badge" viewBox="0 0 74 74"><circle cx="37" cy="37" r="37" fill="url(#badgeFill)"/>
      <g fill="none" stroke="#fff" stroke-width="4.5" stroke-linecap="round" stroke-linejoin="round">
        <path d="M15 33l10-10 8 5 8-4 8 2 10 9"/><path d="M27 41l10 10M32 37l10 10M37 33l10 10M22 45l7 7"/><path d="M59 35L47 45"/></g>
    </svg>
    <h3>Settlement<br>Layer Innovation</h3>
    <p>Ut enim ad minim veniam,<br>quis nostrud exercitation ullamco</p>
  </div>

  <div class="feature f5">
    <svg class="badge" viewBox="0 0 74 74"><circle cx="37" cy="37" r="37" fill="url(#badgeFill)"/>
      <circle cx="45" cy="38" r="15" fill="#fff"/><rect x="43" y="18" width="4" height="6" fill="#fff"/>
      <path d="M45 30v9h7" fill="none" stroke="#fb9a20" stroke-width="2.5"/>
      <g stroke="#fff" stroke-width="3" stroke-linecap="round"><path d="M22 26h5M18 33h8M16 40h10M20 47h8"/></g>
    </svg>
    <h3>Quicker &amp; Safer<br>Settlement for Quillex</h3>
    <p>Ut enim ad minim veniam,<br>quis nostrud exercitation ullamco</p>
  </div>

  <div class="feature f6">
    <svg class="badge" viewBox="0 0 74 74"><circle cx="37" cy="37" r="37" fill="url(#badgeFill)"/>
      <g fill="#fff"><circle cx="37" cy="17" r="5"/><path d="M30 30c0-5 3-7 7-7s7 2 7 7z"/>
        <circle cx="22" cy="41" r="5"/><path d="M14 56c0-5 4-8 8-8s8 3 8 8z"/>
        <circle cx="52" cy="41" r="5"/><path d="M44 56c0-5 4-8 8-8s8 3 8 8z"/></g>
      <g stroke="#fff" stroke-width="2.5" fill="none"><path d="M37 30v8M37 38L25 46M37 38l12 8"/></g>
    </svg>
    <h3>Foreign<br>Stablecoin Network</h3>
    <p>Ut enim ad minim veniam,<br>quis nostrud exercitation ullamco</p>
  </div>
</section>

<section class="partners">
  <h2 class="section-title">Partners</h2>
  <div class="partner-row">
    <div class="partner">pondru</div>
    <div class="partner"><span class="dot"></span>zentrimo</div>
    <div class="partner">lumbrecks</div>
    <div class="partner"><span class="dot"></span>tovern</div>
  </div>
</section>

<section class="newsletter">
  <h2>Subscribe Our Newsletter</h2>
  <p class="note">Lorem Ipsum is simply dummy text of the printing and typesetting industry.</p>
  <div class="email">
    <span>Enter your email</span>
    <svg viewBox="0 0 16 16"><path d="M15 1L1 7l5 2 2 6z" fill="#12275e"/><path d="M15 1L6 9" stroke="#e8e8e8" stroke-width="1"/></svg>
  </div>
</section>

<footer class="footer">
  <div class="brand">Quillex</div>
  <nav class="social"><span>Nook</span><span>Pelt</span><span>Vanta</span><span>Gorv</span></nav>
</footer>

</body>
</html>
```